Web Design for Small Healthcare Startup

Hello,

We are seeking a Website Design for a healthcare company focusing on mobile vaccinations, employee health and wellness services onsite at businesses, and consulting services relating to Healthcare Entities in WA state. Our company’s mission is to “To aid in a healthier workplace”. Brightpath Rovers will provide on-site wellness services to employers that simplify and streamline employee preventative health as well as onsite consulting services to help with compliance of Healthcare Entities.

We are seeking a Website Design for Brightpath Rovers, PLLC. Our company’s mission is to provide mobile health and wellness services to employers onsite at their businesses. These services include mobile vaccinations clinics for employees as well as wellness and health screenings. The company will also offer healtcare compliance consulting services for Healthcare Entities. The company was founded to bring these important healthcare services to businesses and keep employees healthy. Healthy employees are the cornerstone to a great business and we want to help orginazations achieve their goals of having a healthy productive workforce.

We are looking for a moderin website design that will need to be coded. We have attached our current logo design for reference as well as a brief questionare regarding our business for your information (not necessary to include all information). We would like something SEO friendly and easy to navigate.

Thank you!

Brightpath Rovers, PLLC

Target Market(s)

Small Businesses

Industry/Entity Type

Healthcare

Coding

Coded - Design and coding required

Number of Pages Required

1 page

Requirements
Nice to have
• SEO Friendly, Incorporate Logo

```html
<!DOCTYPE html>
<html lang="en">
<head>
<meta charset="utf-8">
<title>Brightpath Rovers, PLLC – Mobile Workplace Wellness</title>
<link href="https://fonts.googleapis.com/css2?family=Arvo:wght@700&family=Poppins:wght@400;500;600;700&display=swap" rel="stylesheet">
<style>
:root{
  --purple:#a2499c;
  --blue:#1b4f9e;
  --ink:#1d1d1d;
  --muted:#5b5b5b;
  --light:#f4f4f4;
  --footer:#101010;
  --white:#ffffff;
}
*{box-sizing:border-box;margin:0;padding:0}
html,body{width:1200px;height:3202px;overflow:hidden}
body{position:relative;font-family:"Poppins",sans-serif;color:var(--ink);background:var(--white)}
.abs{position:absolute}
.btn{position:absolute;display:flex;align-items:center;justify-content:center;height:40px;padding:0 24px;border-radius:20px;background:var(--purple);color:var(--white);font-size:16px;text-decoration:none}
.btn.inline{position:static;display:inline-flex;width:120px;padding:0}
.site-header{position:absolute;left:0;top:0;width:1200px;height:112px;background:var(--white)}
.brand{position:absolute;left:163px;top:38px;display:flex;align-items:center;gap:10px;font-weight:700;font-size:22px;color:var(--blue)}
.brand-dot{width:26px;height:26px;border-radius:50%;background:var(--purple)}
.nav{position:absolute;top:46px;font-size:16px;color:var(--ink)}
.hero{position:absolute;left:0;top:112px;width:1200px;height:526px;background:linear-gradient(90deg,#d6ecf6 0%,#cfe6f1 35%,#9fc0d6 60%,#6f93b5 100%)}
.hero h1{position:absolute;left:163px;top:160px;font-family:"Arvo",serif;font-size:39px;line-height:50px;color:var(--blue)}
.section-light{position:absolute;left:0;width:1200px;background:var(--light)}
.photo-circle{position:absolute;border-radius:50%;border:8px solid var(--white);box-shadow:0 6px 20px rgba(0,0,0,.12)}
.heading{position:absolute;font-weight:700;color:var(--blue)}
.para{position:absolute;font-size:16px;line-height:27px;color:var(--muted);letter-spacing:.6px}
.why-text{position:absolute;left:161px;top:128px;width:450px}
.why-text h2{font-weight:700;color:var(--blue);font-size:36px;line-height:46px;margin-bottom:8px}
.why-text p{font-size:15px;line-height:27px;color:var(--muted);letter-spacing:.3px;margin-bottom:8px}
.why-text .btn{margin-top:14px}
.service{position:absolute;width:220px;height:220px}
.service svg.ring{position:absolute;left:0;top:0}
.service .icon{position:absolute;left:80px;top:48px}
.service p{position:absolute;left:20px;width:180px;top:128px;text-align:center;font-size:15px;line-height:23px;color:var(--muted)}
.site-footer{position:absolute;left:0;top:2875px;width:1200px;height:327px;background:var(--footer);color:var(--white)}
.footer-title{position:absolute;top:58px;font-size:20px;font-weight:600;color:var(--purple)}
.footer-links{position:absolute;left:163px;top:96px;list-style:none;font-size:15px;line-height:30px}
.social{position:absolute;top:3057px;width:36px;height:36px;border-radius:50%;border:1px solid #555}
</style>
</head>
<body>

<header class="site-header">
  <div class="brand"><span class="brand-dot"></span>Brightpath Rovers</div>
  <span class="nav" style="left:537px">Home</span>
  <span class="nav" style="left:622px">About Us</span>
  <span class="nav" style="left:729px">Services</span>
  <span class="nav" style="left:830px">Pricing</span>
  <a class="btn" style="left:919px;top:38px;height:36px;width:120px;padding:0" href="#contact">Contact Us</a>
</header>

<section class="hero">
  <div class="abs" role="img" aria-label="Smiling group of diverse office employees" style="left:500px;top:0;width:700px;height:526px;background:linear-gradient(90deg,rgba(255,255,255,0) 0%,rgba(120,150,185,.5) 40%,rgba(80,110,150,.6) 100%)"></div>
  <h1>Making<br>The Workplace<br>A Healthier Place</h1>
  <a class="btn" style="left:162px;top:330px;width:120px;padding:0" href="#about">More Info</a>
</section>

<section id="about" class="section-light" style="top:638px;height:525px">
  <div class="photo-circle" role="img" aria-label="Mobile vaccine van with a canopy clinic set up on a city street" style="left:163px;top:84px;width:350px;height:350px;background:linear-gradient(160deg,#c47a55 0%,#9a8d80 45%,#3f8f83 65%,#d9d9d9 100%)"></div>
  <h2 class="heading" style="left:601px;top:180px;font-size:36px">About Brightpath Rovers</h2>
  <p class="para" style="left:601px;top:236px;width:450px;font-size:15px;letter-spacing:.3px">Brightpath Rovers is a mobile vaccine clinic providing employers on-site, seamless, hassle-free vaccine clinics for their employees.</p>
  <a class="btn" style="left:601px;top:338px;width:120px;padding:0" href="#">Read More</a>
</section>

<section id="services">
  <svg width="0" height="0" class="abs">
    <defs><linearGradient id="ringGrad" x1="0" y1="0" x2="1" y2="1"><stop offset="0" stop-color="#1b4f9e"/><stop offset="1" stop-color="#a2499c"/></linearGradient></defs>
  </svg>
  <h2 class="heading" style="left:0;width:1200px;text-align:center;top:1286px;font-size:34px">Our Services</h2>

  <div class="service" style="left:225px;top:1378px">
    <svg class="ring" width="220" height="220"><circle cx="110" cy="110" r="107" fill="none" stroke="url(#ringGrad)" stroke-width="4"/></svg>
    <svg class="icon" width="64" height="64" fill="none" stroke="#a2499c" stroke-width="2"><rect x="4" y="10" width="32" height="40"/><path d="M36 26h14l10 12v12H36"/><circle cx="16" cy="54" r="5"/><circle cx="48" cy="54" r="5"/><path d="M20 20v12M14 26h12"/></svg>
    <p>Mobile Vaccine Clinics Providing Flu</p>
  </div>
  <div class="service" style="left:490px;top:1378px">
    <svg class="ring" width="220" height="220"><circle cx="110" cy="110" r="107" fill="none" stroke="url(#ringGrad)" stroke-width="4"/></svg>
    <svg class="icon" width="64" height="64" fill="none" stroke="#a2499c" stroke-width="2"><rect x="6" y="6" width="28" height="52" rx="4"/><path d="M6 20h28M6 44h28"/><circle cx="48" cy="22" r="8"/><path d="M34 50h26M48 44v12"/></svg>
    <p>Covid Booster</p>
  </div>
  <div class="service" style="left:755px;top:1378px">
    <svg class="ring" width="220" height="220"><circle cx="110" cy="110" r="107" fill="none" stroke="url(#ringGrad)" stroke-width="4"/></svg>
    <svg class="icon" width="64" height="64" fill="none" stroke="#a2499c" stroke-width="2"><path d="M32 8v20M32 28c-6 0-10 6-18 8-6 2-8 18-2 20 8 2 16-6 20-14M32 28c6 0 10 6 18 8 6 2 8 18 2 20-8 2-16-6-20-14"/></svg>
    <p>Pneumonia Vaccines</p>
  </div>
  <div class="service" style="left:357px;top:1631px">
    <svg class="ring" width="220" height="220"><circle cx="110" cy="110" r="107" fill="none" stroke="url(#ringGrad)" stroke-width="4"/></svg>
    <svg class="icon" width="64" height="64" fill="none" stroke="#a2499c" stroke-width="2"><path d="M34 34l-10-10a6 6 0 0 1 10-8 6 6 0 0 1 10 8z"/><path d="M32 20v8M28 24h8"/><path d="M6 50l12-10h16a4 4 0 0 1 0 8H24M34 48l16-8a4 4 0 0 1 4 6L38 58H14"/></svg>
    <p>Wellness Screenings</p>
  </div>
  <div class="service" style="left:622px;top:1631px">
    <svg class="ring" width="220" height="220"><circle cx="110" cy="110" r="107" fill="none" stroke="url(#ringGrad)" stroke-width="4"/></svg>
    <svg class="icon" width="64" height="64" fill="none" stroke="#a2499c" stroke-width="2"><rect x="4" y="4" width="30" height="56" rx="3"/><rect x="26" y="10" width="34" height="40" rx="3"/><path d="M43 22v16M35 30h16"/><circle cx="18" cy="24" r="6"/></svg>
    <p>Consulting Services For WA Healthcare Entities</p>
  </div>
</section>

<section class="section-light" style="top:1933px;height:589px">
  <div class="why-text">
    <h2>Why Choose Us?</h2>
    <p>Mobile, traveling clinic comes to you to provide vaccines on-site. Hassle-free, seamless, avoid congested waiting rooms at medical offices and long lines at local pharmacies. Increasing likelihood employees will get vaccinated, reducing workplace illness, sick days, etc. Local, Pharmacist owned and operated.</p>
    <p>Cost Transparency, available flexible hours, accommodating to your business needs, employees, spouses, children = <strong style="color:var(--blue);font-weight:600;letter-spacing:0">less sick days</strong></p>
    <a class="btn inline" href="#contact">Contact Us</a>
  </div>
  <div class="photo-circle" role="img" aria-label="Nurse giving a vaccine shot to a masked young man in a clinic" style="left:689px;top:118px;width:350px;height:350px;background:linear-gradient(150deg,#e8e6e2 0%,#8fb6a5 40%,#a9c4de 70%,#eef2f6 100%)"></div>
</section>

<section>
  <h2 class="heading" style="left:0;width:1200px;text-align:center;top:2606px;font-size:22px">Avoid Long Lines...</h2>
  <p class="para" style="left:0;width:1200px;text-align:center;top:2648px;font-size:15px;letter-spacing:.2px">Each employee can sign up for specific time or dept managers can release employees in phases to clinic.<br>Also available: book for entire day so employees can get vaccinated as their workload permits.</p>
  <p class="para" style="left:0;width:1200px;text-align:center;top:2709px;font-size:15px;letter-spacing:.2px">Employees will avoid congested waiting rooms at medical offices and long lines at local pharmacies.</p>
  <a class="btn" style="left:543px;top:2758px;width:120px;padding:0" href="#contact">Contact Us</a>
</section>

<footer id="contact" class="site-footer">
  <div class="footer-title" style="left:163px">Quick Links</div>
  <ul class="footer-links">
    <li>• Home</li><li>• About Us</li><li>• Services</li><li>• Pricing</li><li>• Contact Us</li>
  </ul>
  <div class="abs" style="left:0;width:1200px;top:124px;text-align:center;font-weight:700;font-size:22px;color:#3b72c9">Brightpath Rovers</div>
  <div class="footer-title" style="left:810px">Contact Details</div>
  <svg class="abs" style="left:810px;top:102px" width="38" height="38" fill="none" stroke="#2d63b8" stroke-width="1.5"><circle cx="19" cy="19" r="18"/><path d="M13 11l4 0 2 5-3 2a11 11 0 0 0 5 5l2-3 5 2v4a2 2 0 0 1-2 2A16 16 0 0 1 11 13a2 2 0 0 1 2-2z"/></svg>
  <div class="abs" style="left:858px;top:103px;font-size:14px;line-height:18px"><strong>Phone</strong><br>123-456-7890</div>
  <svg class="abs" style="left:810px;top:160px" width="38" height="38" fill="none" stroke="#2d63b8" stroke-width="1.5"><circle cx="19" cy="19" r="18"/><rect x="10" y="13" width="18" height="12"/><path d="M10 13l9 7 9-7"/></svg>
  <div class="abs" style="left:858px;top:161px;font-size:14px;line-height:18px"><strong>Email</strong><br>info@brightpathrovers.com</div>
  <div class="abs" style="left:163px;top:263px;width:874px;height:1px;background:#3a3a3a"></div>
  <div class="abs" style="left:0;width:1200px;top:285px;text-align:center;font-size:13px">© 2022 Brightpath Rovers, PLLC. All Rights Reserved.</div>
</footer>
<span class="social" style="left:480px" aria-label="Social profile"></span>
<span class="social" style="left:527px" aria-label="Social profile"></span>
<span class="social" style="left:573px" aria-label="Social profile"></span>

</body>
</html>
```